Business Card Design

We are a new residential construction company.our team is made up of young highly skilled tradesman of the next generation of carpenters coming through with new skills and ideas.we chose the name meridian as it means strikingly different from the rest as this is what we plan to be and we would like to portray this in our business card.we like Bold lettering as we want to make a statement, also the use of colour would be great as we want to stand out from the usual plain construction cards and logos.
I have attached a logo sketch I did as a rough idea if you can tidy it up or improve on it would be good.
I have also attached the LBP logo please include this on the card small but still legible.
open to any colourschemes ideas.
thanks
(note)please delete the LBP#804317 off from the card details please.
Industry/Entity Type
Construction
Contact Information for Business Card
MERIDIAN CONSTRUCTION LIMITED
Director:Tom Halvick
Mobile :0217364820
Email:Meridian.Construction@quillpost.example
Address:48 Wendle place,Ashgrove park 2091,Auckland
LBP#BP804317

```html
<!DOCTYPE html>
<html lang="en">
<head>
<meta charset="utf-8">
<title>Meridian Construction – Business Card</title>
<link rel="stylesheet" href="https://fonts.googleapis.com/css2?family=Open+Sans:wght@400;700&display=swap">
<style>
  :root {
    --page: #e4e4e4;
    --card-dark: #2a2a2a;
    --card-light: #ffffff;
    --navy: #1f1d5c;
    --cyan: #3cb9d6;
    --ink: #333333;
  }
  * { box-sizing: border-box; margin: 0; padding: 0; }
  html, body {
    width: 1200px; height: 985px; overflow: hidden;
    background: var(--page);
    font-family: "Open Sans", Arial, sans-serif;
  }
  .card {
    position: absolute; left: 320px;
    width: 560px; height: 320px;
    border-radius: 24px; overflow: hidden;
    box-shadow: 0 6px 18px rgba(0,0,0,0.18);
  }
  .card-back { top: 100px; background: var(--card-dark); }
  .card-front { top: 480px; background: var(--card-light); }

  .back-name {
    position: absolute; inset: 0;
    display: flex; align-items: center; justify-content: center; gap: 16px;
    color: #ffffff; font-weight: 700; font-size: 60px; letter-spacing: 1px;
  }
  .back-name .mark { width: 22px; height: 22px; background: #ffffff; }

  .front-band { position: absolute; inset: 0; }
  .front-band polygon { fill: var(--card-dark); }

  .front-name {
    position: absolute; left: 120px; top: 34px;
    display: flex; align-items: center; gap: 12px;
    background: var(--card-light);
    padding: 8px 18px;
    color: var(--navy); font-weight: 700; font-size: 46px;
  }
  .front-name .mark { width: 18px; height: 18px; background: var(--navy); }

  .details {
    position: absolute; left: 140px; top: 136px; right: 30px;
    color: var(--ink); font-size: 13.5px; line-height: 1.45;
  }
  .person { color: var(--navy); font-size: 23px; line-height: 1.1; }
  .role { color: var(--cyan); font-size: 13px; margin-bottom: 4px; }
  .company {
    color: var(--navy); font-size: 13px; text-transform: uppercase;
    padding-bottom: 4px; border-bottom: 1px solid var(--cyan); margin-bottom: 6px;
  }

  .contact-icon {
    position: absolute; left: 46px; width: 14px; height: 14px;
    border-radius: 2px; background: var(--cyan);
  }
  .contact-icon svg { display: block; width: 14px; height: 14px; }
  .icon-phone { top: 236px; }
  .icon-mail { top: 256px; }
</style>
</head>
<body>

<section class="card card-back">
  <div class="back-name"><span class="mark"></span>meridian</div>
</section>

<section class="card card-front">
  <svg class="front-band" viewBox="0 0 560 320" preserveAspectRatio="none" aria-hidden="true">
    <polygon points="0,0 250,0 250,96 70,176 70,320 0,320"/>
  </svg>

  <div class="front-name"><span class="mark"></span>meridian</div>

  <div class="details">
    <p class="person">Tom Halvick</p>
    <p class="role">Director</p>
    <p class="company">MERIDIAN CONSTRUCTION LIMITED</p>
    <p>48 Wendle place,Ashgrove park 2091,Auckland LBP#BP804317</p>
    <p>0217364820</p>
    <p>Meridian.Construction@quillpost.example</p>
  </div>

  <span class="contact-icon icon-phone">
    <svg viewBox="0 0 14 14" aria-hidden="true">
      <path d="M4 3 L5.5 3 L6.2 5 L5.2 5.8 Q6 7.8 8.2 8.8 L9 7.8 L11 8.5 L11 10 Q10.5 11 9.5 11 Q4 10.5 3 4.5 Q3 3.5 4 3 Z" fill="#1f1d5c"/>
    </svg>
  </span>
  <span class="contact-icon icon-mail">
    <svg viewBox="0 0 14 14" aria-hidden="true">
      <rect x="3" y="4" width="8" height="6" fill="none" stroke="#1f1d5c" stroke-width="1.2"/>
      <path d="M3 4 L7 7.5 L11 4" fill="none" stroke="#1f1d5c" stroke-width="1.2"/>
    </svg>
  </span>
</section>

</body>
</html>
```